Business Card Design Project

Our logo/name is trademarked (since around 2000) and is owned by us. Logo originally designed in 1984 by my wife. Our logo needs freshening up while retaining its recognizability and trademark coverage. Our business cards, line card etc., web page home also need freshening, maybe as simple as inserting the updated logo, or completely redesigned.

Our logo represents "torque", which is defined as a force around an axis or "twist". Since 1949, we have been one of the world leaders in Norlane industrial clutches and brakes sales and service. We specialize in heavy duty applications such as stamping presses, steel mills, paper mills, drilling rigs etc. We are engineers as well as business people. Our customers are maintenance supervisors, plant engineers, small business owners. Our "color" has been reflex blue For more background, our website is www.brindlemark-co.com
Updates

I have posted a correct scan of the card/logo front and some previous versions of our logo.  (For now skip the back.)

As my brief said, we are after refreshing the logo and our cards/literature but the logo and card first.

Project Deadline Extended
Reason: I had trouble getting my existing logo scanned. should be up now.

Hopefully, the third try loading my existing logo and card worked!  The "City" banner had been on the0 bottom of the card.

Alt. A:  leave cities off
Alt B.  Instead of the cities, take a look at our web site home page or second page showing the world map and see if the world (as a territory which we do ship worldwide) could be worked in or highlight the back of the
 card with lines and the world? 

Future project will be line card redesign and web site
with separate project budget etc.www.brindlemark-co.com

Project Deadline Extended
Reason: My business partner was out of town last week and I wanted a couple days for his input. Thank you for your patience

Thank you all for your input! Dale Hurst

Target Market(s)

factory maintenance managers, plant engineers, small business owners

Industry/Entity Type

Small Business

Requirements
Must have
• clear development of existing trademarked logo

```html
<!DOCTYPE html>
<html lang="en">
<head>
<meta charset="utf-8">
<title>Brindlemark Inc. Business Card</title>
<link href="https://fonts.googleapis.com/css2?family=Libre+Caslon+Text:wght@700&family=Sorts+Mill+Goudy&display=swap" rel="stylesheet">
<style>
  :root {
    --frame: #000000;
    --card: #ffffff;
    --reflex-blue: #0d4da0;
    --ink: #141414;
  }
  * { margin: 0; padding: 0; box-sizing: border-box; }
  html, body {
    width: 1200px;
    height: 813px;
    overflow: hidden;
    background: var(--frame);
  }
  .card {
    position: absolute;
    left: 19px;
    top: 19px;
    width: 1162px;
    height: 775px;
    background: var(--card);
    overflow: hidden;
    font-family: "Sorts Mill Goudy", Georgia, serif;
    color: var(--ink);
  }
  .accent-stripe {
    position: absolute;
    left: 67px;
    top: 0;
    width: 39px;
    height: 100%;
    background: linear-gradient(to right, var(--reflex-blue) 0%, var(--reflex-blue) 80%, rgba(13,77,160,0.35) 100%);
  }
  .brand {
    position: absolute;
    right: 40px;
    top: 96px;
    display: flex;
    align-items: center;
    gap: 18px;
  }
  .brand-dot {
    width: 44px;
    height: 44px;
    border-radius: 50%;
    background: var(--reflex-blue);
  }
  .brand-name {
    font-family: "Sorts Mill Goudy", Georgia, serif;
    font-size: 58px;
    line-height: 1;
    color: var(--reflex-blue);
  }
  .person {
    position: absolute;
    left: 140px;
    top: 218px;
  }
  .person-name {
    font-family: "Libre Caslon Text", Georgia, serif;
    font-weight: 700;
    font-size: 42px;
    line-height: 1.15;
  }
  .person-title {
    font-size: 38px;
    line-height: 1.3;
  }
  .contact {
    position: absolute;
    right: 28px;
    top: 446px;
    text-align: right;
    font-size: 38px;
    line-height: 52px;
  }
  .contact .hotline { margin-top: 8px; }
  .contact .email { font-size: 42px; line-height: 58px; }
</style>
</head>
<body>
  <div class="card">
    <div class="accent-stripe"></div>

    <div class="brand">
      <span class="brand-dot"></span>
      <span class="brand-name">Brindlemark Inc.</span>
    </div>

    <div class="person">
      <div class="person-name">Dale Hurst</div>
      <div class="person-title">President</div>
    </div>

    <div class="contact">
      <div class="street">2280 N. Cedar Ridge, Suite 240</div>
      <div class="city">Ashford, MI 48190-2204</div>
      <div class="phone">(248) 555-0143</div>
      <div class="fax">Fax (248) 555-0178</div>
      <div class="hotline">Parts Hot Line (800) 555-0162</div>
      <div class="email">E-Mail: dhurst@brindlemark-co.com</div>
    </div>
  </div>
</body>
</html>
```